Ironvale Leasing Corp - Business Card Design

Need a new modern designed business card that is different and stands out to represent my equipment financing company. Ironvale Leasing Corp finances all types of equipment and all types of industries. We like to do equipment financing a different way by putting customers first and want our card to represent that different approach to business. I want a card that some remembers when they receive it so it sticks in their mind and makes that wow impression.

Card should have a black background so the logo stands out. It can be horizontial or vertical or a combination of both.

Front of card information is below that shows the information that would go on my card. That is where I want a different look or design to stand out. The front could be split black/orange colour so the logo could pop on black side and information on orange side with different lettering. Just outside the box thinking on the front of the card. Open to any type of design.

Back of card is below which i I like unless you have a different spin to provide or a different idea that would make the card better as I am open to anything that looks great.

Target Market(s)

Ironvale Leasing Corp deals with business owners in all industries.

Industry/Entity Type

Business

Contact Information for Business Card

Colors

Designer to choose colors to be used in the design.

Requirements
Must have
• Modern
• Different
• Stand Out
• Makes an Impression

```html
<!DOCTYPE html>
<html lang="en">
<head>
<meta charset="UTF-8">
<title>Ironvale Leasing Corp – Business Cards</title>
<link href="https://fonts.googleapis.com/css2?family=Lato:wght@400;700&display=swap" rel="stylesheet">
<style>
  :root {
    --stage: #2b2b2d;
    --card: #000000;
    --orange: #f26a1b;
    --orange-deep: #e3401c;
    --orange-light: #ff8a2a;
    --white: #ffffff;
    --grey: #b9b9b9;
  }
  * { margin: 0; padding: 0; box-sizing: border-box; }
  html, body { width: 1200px; height: 800px; overflow: hidden; }
  body {
    background: var(--stage);
    font-family: "Lato", sans-serif;
    display: flex;
    align-items: center;
    justify-content: center;
    gap: 60px;
  }
  .card {
    position: relative;
    width: 460px;
    height: 460px;
    background: var(--card);
    overflow: hidden;
    box-shadow: 0 14px 30px rgba(0,0,0,0.45);
  }
  .brand-name {
    color: var(--orange);
    font-weight: 400;
    text-transform: uppercase;
    letter-spacing: 0.08em;
    line-height: 1.15;
  }
  /* Back */
  .card-back {
    display: flex;
    align-items: center;
    justify-content: center;
  }
  .card-back .brand {
    display: flex;
    align-items: center;
    gap: 18px;
  }
  .card-back .brand-mark {
    width: 22px;
    height: 22px;
    background: var(--orange);
  }
  .card-back .brand-name { font-size: 34px; }
  /* Front */
  .card-front .brand-name {
    position: absolute;
    top: 56px;
    right: 44px;
    font-size: 30px;
    text-align: right;
  }
  .contact {
    position: absolute;
    top: 176px;
    right: 44px;
    text-align: right;
    color: var(--white);
  }
  .contact .person {
    font-weight: 700;
    font-size: 24px;
    letter-spacing: 0.02em;
    text-transform: uppercase;
  }
  .contact .role {
    font-size: 15px;
    letter-spacing: 0.06em;
    text-transform: uppercase;
    margin-bottom: 18px;
  }
  .contact .line { font-size: 15px; line-height: 1.45; }
  .contact .web { color: var(--orange); }
  .swoosh {
    position: absolute;
    left: 0;
    bottom: 0;
    width: 460px;
    height: 120px;
  }
</style>
</head>
<body>
  <section class="card card-back">
    <div class="brand">
      <span class="brand-mark"></span>
      <span class="brand-name">Ironvale<br>Leasing Corp</span>
    </div>
  </section>

  <section class="card card-front">
    <div class="brand-name">Ironvale<br>Leasing Corp</div>
    <div class="contact">
      <div class="person">Dane Morrow</div>
      <div class="role">President</div>
      <div class="line">403.555.0192</div>
      <div class="line">dane@ironvaleleasing.ca</div>
      <div class="line web">www.ironvaleleasing.ca</div>
    </div>
    <svg class="swoosh" viewBox="0 0 460 120" preserveAspectRatio="none" aria-hidden="true">
      <defs>
        <linearGradient id="band" x1="0" y1="0" x2="1" y2="0">
          <stop offset="0" stop-color="var(--orange-deep)"/>
          <stop offset="1" stop-color="var(--orange-light)"/>
        </linearGradient>
      </defs>
      <path d="M0 60 C140 100 300 110 460 20 L460 120 L0 120 Z" fill="var(--white)"/>
      <path d="M0 74 C150 110 310 118 460 44 L460 120 L0 120 Z" fill="var(--card)"/>
      <path d="M0 84 C160 118 320 122 460 56 L460 120 L0 120 Z" fill="url(#band)"/>
    </svg>
  </section>
</body>
</html>
```